FRESH WEB DESIGN FOR A HEALTH - SOCIAL NETWORK

We are currently looking for a creative, fresh, vibrant, inspiring design for a new social network focused on health and nutrition for health professionals (namely nutritionists) and end-users.

Design requirements - IMPORTANT: please see attached file 'LumaCrest web site design scope' for the detailed brief.

The web site requires new design templates with inter-changeable banners and in some cases profile images. It's important for the website to communicate LumaCrest's core values and image which includes fun, vitality, freshness, life fulfillment, trust, integrity and loyalty to the two target groups. Imagery must have a consistent/inter-related theme across all communities, topics and resources, which need to be easily applied to the web site.To help engage our audience we are looking for something fresh and unique in the selected imagery/ theme/ design templates.

The chosen design will need to be applied to create a PDF, PowerPoint and business card template.

Please see attached file 'LumaCrest web site design scope' to view the LumaCrest web site, which is currently under development.

Nutrition

```html
<!DOCTYPE html>
<html lang="en">
<head>
<meta charset="utf-8">
<title>LumaCrest — Blog</title>
<link href="https://fonts.googleapis.com/css2?family=Exo:wght@400;500;600;700&display=swap" rel="stylesheet">
<style>
  :root {
    --brand-green: #8cc63f;
    --brand-blue: #1a8ad0;
    --nav-blue: #1b86c8;
    --signup-orange: #f7a535;
    --ink: #111111;
    --muted: #8a8a8a;
    --page-grey: #f4f4f4;
    --white: #ffffff;
    --video-bg: rgba(30, 30, 32, 0.78);
  }
  * { box-sizing: border-box; margin: 0; padding: 0; }
  html, body {
    width: 1200px; height: 989px; overflow: hidden;
    font-family: "Exo", sans-serif; background: var(--page-grey);
  }
  .site-header {
    position: absolute; top: 0; left: 0; width: 1200px; height: 77px;
    background: var(--white);
  }
  .brand {
    position: absolute; left: 167px; top: 18px;
    display: flex; align-items: center; gap: 8px;
    font-weight: 600; font-size: 34px; color: var(--brand-green);
    text-decoration: none; letter-spacing: -0.5px;
  }
  .brand-dot { width: 30px; height: 30px; border-radius: 50%; background: var(--brand-blue); }
  .main-nav { position: absolute; top: 28px; left: 567px; display: flex; align-items: center; }
  .main-nav a {
    font-size: 14px; font-weight: 500; color: var(--nav-blue);
    text-decoration: none; margin-right: 25px; line-height: 24px; position: relative;
  }
  .main-nav a.is-active { color: var(--brand-green); }
  .main-nav a.is-active::after {
    content: ""; position: absolute; left: 0; right: 0; bottom: -3px;
    height: 2px; background: var(--brand-green);
  }
  .main-nav a.signup {
    position: absolute; left: 393px; top: -1px; margin: 0;
    width: 84px; height: 28px; line-height: 28px; text-align: center;
    background: var(--signup-orange); color: var(--white); font-weight: 600;
  }
  .hero { position: absolute; top: 77px; left: 0; width: 1200px; height: 475px; overflow: hidden; }
  .hero-photo {
    position: absolute; inset: 0;
    background: linear-gradient(180deg, #2f56b0 0%, #4a72c2 40%, #8a7d5a 62%, #7c6a44 80%, #b59a6e 100%);
  }
  .hero-title {
    position: absolute; left: 167px; top: 54px;
    font-size: 51px; font-weight: 700; line-height: 54px; color: var(--white);
    letter-spacing: -0.3px;
  }
  .hero-button {
    position: absolute; left: 167px; top: 233px; width: 118px; height: 36px;
    border-radius: 18px; background: var(--brand-blue); color: var(--white);
    font-size: 14px; font-weight: 600; line-height: 36px; text-align: center;
    text-decoration: none;
  }
  .video-label {
    position: absolute; left: 767px; top: 222px;
    font-size: 13px; font-weight: 600; color: var(--white);
  }
  .video-frame {
    position: absolute; left: 767px; top: 259px; width: 277px; height: 156px;
    background: var(--video-bg);
  }
  .video-frame svg { position: absolute; left: 105px; top: 45px; }
  .content {
    position: absolute; top: 552px; left: 99px; width: 1012px; height: 437px;
    background: var(--white);
  }
  .section-title {
    position: absolute; left: 68px; top: 40px;
    font-size: 27px; font-weight: 400; color: var(--ink);
  }
  .post-grid { position: absolute; left: 68px; top: 95px; display: flex; }
  .post-card { position: relative; width: 292px; height: 292px; overflow: hidden; }
  .post-card:last-child { width: 293px; }
  .post-photo { position: absolute; inset: 0; }
  .post-card--weight .post-photo { background: linear-gradient(160deg, #3a6aa8 0%, #2c5a98 50%, #4a78a8 100%); }
  .post-card--random .post-photo { background: linear-gradient(160deg, #f6f4f0 0%, #f1ede6 60%, #ebe6de 100%); }
  .post-card--image .post-photo { background: linear-gradient(160deg, #8a6a4a 0%, #c9a88a 40%, #6f9a3a 75%, #ece9e4 100%); }
  .post-category { position: absolute; left: 21px; top: 20px; font-size: 13px; }
  .post-title {
    position: absolute; left: 21px; top: 55px; width: 250px;
    font-size: 27px; font-weight: 400; line-height: 34px;
  }
  .post-link { position: absolute; left: 22px; top: 257px; font-size: 13px; text-decoration: none; }
  .post-card--weight .post-category,
  .post-card--weight .post-title,
  .post-card--weight .post-link { color: var(--white); }
  .post-card--random .post-category,
  .post-card--random .post-title { color: var(--ink); }
  .post-card--random .post-link { color: var(--nav-blue); }
  .more-stories {
    position: absolute; left: 0; right: 0; top: 414px; text-align: center;
    font-size: 13px; font-weight: 500; color: var(--muted); text-decoration: none;
  }
</style>
</head>
<body>
  <header class="site-header">
    <a class="brand" href="#"><span class="brand-dot"></span>LumaCrest</a>
    <nav class="main-nav">
      <a href="#">home</a>
      <a href="#" class="is-active">blog</a>
      <a href="#">about</a>
      <a href="#">products</a>
      <a href="#">network</a>
      <a href="#">contact</a>
      <a href="#" class="signup">signup</a>
    </nav>
  </header>

  <section class="hero">
    <div class="hero-photo" role="img" aria-label="Runner in red shirt striding across dry mountain hills under a blue sky"></div>
    <h1 class="hero-title">Nutrition, Energy,<br>Wellness, Excercise<br>and Great Minds.</h1>
    <a class="hero-button" href="#">Read more.</a>
    <p class="video-label">Watch our brand new video</p>
    <div class="video-frame" role="img" aria-label="Video preview of a woman stretching outdoors">
      <svg width="68" height="68" viewBox="0 0 68 68" aria-hidden="true">
        <circle cx="34" cy="34" r="30" fill="none" stroke="#1a8ad0" stroke-width="5"/>
        <path d="M26 20 L49 34 L26 48 Z" fill="#1a8ad0"/>
      </svg>
    </div>
  </section>

  <main class="content">
    <h2 class="section-title">An ordinary blog.</h2>
    <div class="post-grid">
      <article class="post-card post-card--weight">
        <div class="post-photo" role="img" aria-label="Woman in sprint start position on a beach, blue tint"></div>
        <p class="post-category">Category / Weight</p>
        <h3 class="post-title">10 Weight Loss Bloggers You Should Follow</h3>
        <a class="post-link" href="#">Read more →</a>
      </article>
      <article class="post-card post-card--random">
        <div class="post-photo" role="img" aria-label="Faded photo of a woman eating an apple"></div>
        <p class="post-category">Category / Random</p>
        <h3 class="post-title">The Incredible Weight Loss Photo 'Contour' Magazine</h3>
        <a class="post-link" href="#">Read more →</a>
      </article>
      <article class="post-card post-card--image">
        <div class="post-photo" role="img" aria-label="Smiling woman in green shirt with a towel at the gym"></div>
      </article>
    </div>
    <a class="more-stories" href="#">For more blog stories click here</a>
  </main>
</body>
</html>
```